Home page design for car dealership (Brightway Autohaus - 1585)

The client wants to update his current website: http://www.brightwayautohaus-example.com/
You can find the dealer info on their current site.

Please use the instructions provided by the dealer to provide new design mockups:

ridgecrestcars-example.com- use the main background

harlowpinemotors-example.com - wants a large slideshow with 4 large buttons below it: Inventory, Contact Us, Tradeloft Vehicles and Chatterbook. Use 2 of their showroom pictures for the button images. For Tradeloft and Chatterbook, keep the company's logo

Have fun and let me know if there's any questions!
Updates

Hello everyone! I've sent the mockups provided to the client and as soon as I get feedback, I will notify you individually of their decision, or revisions, if needed. Thanks so much for your patience! Maribel

Industry/Entity Type

Dealership

```html
<!DOCTYPE html>
<html lang="en">
<head>
<meta charset="utf-8">
<title>Brightway Autohaus</title>
<link href="https://fonts.googleapis.com/css2?family=Oswald:wght@300;400&family=Michroma&display=swap" rel="stylesheet">
<style>
:root{
  --ink:#ffffff;
  --ink-soft:#e4e4e4;
  --stone-dark:#1c1c1c;
  --stone-mid:#4a4a4a;
  --stone-light:#7a7a7a;
  --nav-bg:#9b9b9b;
  --nav-line:#b5b5b5;
  --panel:#8e8e8e;
  --tile-dark:#333333;
  --label:#a3a3a3;
}
*{margin:0;padding:0;box-sizing:border-box}
html,body{width:1200px;height:1197px;overflow:hidden}
body{
  position:relative;
  font-family:'Oswald',sans-serif;
  color:var(--ink);
  background:
    radial-gradient(ellipse 700px 320px at 600px 250px, rgba(140,140,140,.55), transparent 70%),
    linear-gradient(to bottom,#3a3a3a 0,#6a6a6a 180px,#5c5c5c 520px,#3a3a3a 700px,#111 790px,#2b2b2b 860px,#4d4d4d 1000px,#3c3c3c 1197px);
}
.logo{position:absolute;left:184px;top:58px;font-size:36px;font-weight:400;letter-spacing:3px;color:var(--ink-soft);text-transform:uppercase}
.dealer-info{position:absolute;right:184px;top:54px;text-align:right;font-family:'Michroma',sans-serif;color:var(--ink-soft)}
.dealer-info .phone{font-size:17px;color:var(--ink)}
.dealer-info .addr{font-size:10px;line-height:13px}
.main-nav{position:absolute;left:184px;top:159px;width:832px;height:38px;display:flex;background:var(--nav-bg)}
.main-nav a{color:var(--ink);text-decoration:none;font-size:13px;display:flex;align-items:center;justify-content:center;border-left:1px solid var(--nav-line)}
.main-nav a:first-child{border-left:0}
.hero{position:absolute;left:184px;top:227px;width:832px;height:300px;
  background:linear-gradient(to bottom,#9c8d7a 0,#cfc4b3 25%,#8f8373 55%,#5f564c 100%);
  box-shadow:0 18px 30px rgba(0,0,0,.45)}
.hero .arrow{position:absolute;top:139px}
.hero .dots{position:absolute;left:392px;bottom:10px;display:flex;gap:6px}
.hero .dots span{width:8px;height:8px;border-radius:50%;background:rgba(255,255,255,.35)}
.hero .dots span:first-child{background:#fff}
.tile{position:absolute;top:576px;width:191px;height:131px;overflow:hidden}
.tile .photo{position:absolute;inset:0;background:linear-gradient(135deg,#c79a55,#6b4d33 45%,#2a2220)}
.tile.brand{background:var(--tile-dark)}
.tile .brand-name{position:absolute;left:0;right:0;top:38px;text-align:center;font-size:16px;letter-spacing:1px;text-transform:uppercase;color:var(--ink)}
.tile .label{position:absolute;left:0;bottom:0;height:28px;width:150px;font-size:15px;padding-left:22px;line-height:28px;color:var(--ink);
  background:var(--label);clip-path:polygon(0 0,124px 0,150px 100%,0 100%)}
.tile .label-rest{position:absolute;left:0;right:0;bottom:0;height:4px;background:var(--label)}
.welcome-title{position:absolute;left:397px;width:619px;top:750px;text-align:center;font-size:20px;font-weight:400}
.contact-card{position:absolute;left:184px;top:781px;width:191px;height:258px;background:var(--panel);
  border-left:4px solid #d8d8d8;border-right:4px solid #d8d8d8;text-align:center;box-shadow:0 12px 24px rgba(0,0,0,.45)}
.contact-card h3{font-size:16px;font-weight:400;margin-top:12px;display:flex;align-items:center;justify-content:center;gap:6px}
.contact-card p{font-size:12.5px;font-weight:300;line-height:18px}
.contact-card .block{margin-top:12px}
.intro{position:absolute;left:397px;width:619px;top:805px;text-align:center;font-size:10px;font-weight:300;line-height:18px}
.intro p+p{margin-top:18px}
.thumb{position:absolute;top:945px;width:120px;height:75px}
.more{position:absolute;left:980px;top:971px}
.footer-rule{position:absolute;left:184px;width:832px;top:1142px;height:1px;background:#8a8a8a}
.footer{position:absolute;left:184px;width:832px;top:1162px;display:flex;justify-content:space-between;font-size:10.5px;font-weight:300}
</style>
</head>
<body>
<div class="logo">Brightway Autohaus</div>
<div class="dealer-info">
  <div class="phone">512-555-0147</div>
  <div class="addr">4820 HARLAN CREEK RD<br>AUSTIN, TX 78799</div>
</div>

<nav class="main-nav">
  <a href="#" style="width:119px">Home</a>
  <a href="#" style="width:179px">Inventory</a>
  <a href="#" style="width:178px">Vehicle Finder</a>
  <a href="#" style="width:178px">Financing</a>
  <a href="#" style="width:178px">Contact Us</a>
</nav>

<section class="hero" role="img" aria-label="Slideshow photo of a black coupe parked on a gravel lot">
  <svg class="arrow" style="left:22px" width="24" height="24" viewBox="0 0 24 24"><circle cx="12" cy="12" r="12" fill="rgba(255,255,255,.35)"/><path d="M14 7l-5 5 5 5" stroke="#fff" stroke-width="2" fill="none"/></svg>
  <svg class="arrow" style="right:22px" width="24" height="24" viewBox="0 0 24 24"><circle cx="12" cy="12" r="12" fill="rgba(255,255,255,.35)"/><path d="M10 7l5 5-5 5" stroke="#fff" stroke-width="2" fill="none"/></svg>
  <div class="dots"><span></span><span></span><span></span><span></span></div>
</section>

<a class="tile" style="left:184px" href="#">
  <div class="photo" role="img" aria-label="Showroom photo with rows of sports cars"></div>
  <div class="label">Inventory</div>
</a>
<a class="tile" style="left:397px" href="#">
  <div class="photo" role="img" aria-label="Showroom photo with a convertible in front"></div>
  <div class="label">Contact Us</div>
</a>
<a class="tile brand" style="left:611px" href="#">
  <div class="brand-name">Brightway Autohaus</div>
  <div class="label">Tradeloft Vehicles</div>
</a>
<a class="tile brand" style="left:825px" href="#">
  <div class="brand-name">Brightway Autohaus</div>
  <div class="label">Chatterbook</div>
</a>

<h2 class="welcome-title">WELCOME TO BRIGHTWAY AUTOHAUS</h2>

<aside class="contact-card">
  <h3><svg width="16" height="11" viewBox="0 0 16 11"><rect x=".5" y=".5" width="15" height="10" fill="#fff"/><path d="M.5 .5l7.5 6 7.5-6" stroke="#8e8e8e" fill="none"/></svg>CONTACT</h3>
  <div class="block"><p>BRIGHTWAY AUTOHAUS<br>4820 Harlan Creek Rd<br>Austin, TX 78799<br>512 - 555 - 0147</p></div>
  <h3 style="margin-top:20px"><svg width="14" height="14" viewBox="0 0 14 14"><circle cx="7" cy="7" r="6" stroke="#fff" stroke-width="1.6" fill="none"/><path d="M7 3.5V7h3" stroke="#fff" stroke-width="1.6" fill="none"/></svg>HOURS</h3>
  <div class="block"><p>Monday-Friday: 9 - 6 PM<br>Saturday: 10 - 3 PM<br>Sunday: Closed</p></div>
</aside>

<section class="intro">
  <p>Brightway Autohaus has been the premier dealership in the super car culture of Austin Texas for the last 27 years. We specialize in unique and exotic cars exclusively picked by the owner and car enthusiast himself, Devin Castellan<br>(known and endeared as DC).</p>
  <p>DC takes great pride in the quality of his inventory. As a second generation luxury car dealership owner, his knowledge and experience is unparalleled. Whether you are in the market for an exotic super car, a modified street car, or a reliable family vehicle, we are excited to share our passion with you.</p>
</section>

<div class="thumb" style="left:397px;background:linear-gradient(#b07a66,#d9d2cc)" role="img" aria-label="White sports coupe in front of a building"></div>
<div class="thumb" style="left:539px;background:linear-gradient(#9aa6b0,#b44040 60%,#888)" role="img" aria-label="Red sports coupe at a car meet"></div>
<div class="thumb" style="left:682px;background:linear-gradient(#3a3a3a,#cfcfcf 60%,#999)" role="img" aria-label="White sports coupe on a driveway"></div>
<div class="thumb" style="left:825px;background:linear-gradient(#8e9aa3,#e5e5e5 60%,#a8a8a8)" role="img" aria-label="White coupe in a parking lot"></div>
<svg class="more" width="24" height="24" viewBox="0 0 24 24"><circle cx="12" cy="12" r="11" stroke="#aaa" fill="none"/><path d="M10 8l4 4-4 4" stroke="#aaa" stroke-width="1.5" fill="none"/></svg>

<div class="footer-rule"></div>
<footer class="footer">
  <span>Copyright © 2003-2014 Gearline Web, LTD. All Rights Reserved.</span>
  <span>Home | Inventory | Site Map | Contact Us</span>
  <span>4820 Harlan Creek Rd, Austin , Texas 78799 &nbsp; 512-555-0147</span>
</footer>
</body>
</html>
```